" Oferecemos serviço de elaboração de planejamento e orçamento de obras, acompanhamento de reformas, vistorias e elaboração de laudos e pareces, projetos para empreendimentos residenciais e comerciais (fundações, arquitetônico, estrutural, elétrico, hidrossanitário, telecomunicação, gesso, piso, gás, entre outros), consultoria para implantar sistemas de gestão de produtos e processos, análise da viabilidade econômico-financeira, levando em conta estimativa de custos e mercado de trabalho e por fim, administração de obras, incluindo acompanhamento de obras, contratação da mão de obra e controle de orçamento. "

```html
<!DOCTYPE html>
<html lang="pt-BR">
<head>
<meta charset="UTF-8">
<title>Vertix Engenharia – Cartão de visita</title>
<link href="https://fonts.googleapis.com/css2?family=Arimo:wght@400;700&display=swap" rel="stylesheet">
<style>
  :root {
    --navy: #143f5a;
    --teal: #3aa5b8;
    --white: #ffffff;
    --ink: #1d1d1d;
    --muted: #444444;
    --stage: #e8e5e1;
  }
  html, body {
    margin: 0;
    padding: 0;
    width: 1200px;
    height: 1200px;
    overflow: hidden;
    background: var(--stage);
    font-family: "Arimo", Arial, sans-serif;
  }
  .business-card {
    position: absolute;
    left: 91px;
    top: 463px;
    width: 1018px;
    height: 262px;
    background: var(--white);
    box-shadow: 0 10px 30px rgba(0,0,0,0.18);
    overflow: hidden;
  }
  .card-shapes {
    position: absolute;
    inset: 0;
  }
  .brand {
    position: absolute;
    left: 0;
    width: 430px;
    top: 150px;
    text-align: center;
    color: var(--white);
    font-weight: 700;
    font-size: 30px;
    line-height: 1.2;
    white-space: nowrap;
  }
  .contact-item {
    position: absolute;
    left: 526px;
    display: flex;
    align-items: center;
    gap: 22px;
    white-space: nowrap;
    font-size: 15px;
    color: var(--ink);
  }
  .contact-item .icon {
    width: 26px;
    height: 26px;
    flex: none;
  }
  .contact-item.email { top: 50px; }
  .contact-item.phone { top: 93px; }
  .contact-item.web { top: 146px; }
  .contact-item.address { top: 206px; line-height: 1.2; }
  .contact-person {
    position: absolute;
    left: 727px;
    top: 83px;
    width: 260px;
    text-align: center;
  }
  .contact-person .name {
    font-size: 26px;
    font-weight: 700;
    color: var(--ink);
    line-height: 1;
  }
  .contact-person .role {
    font-size: 12px;
    letter-spacing: 2px;
    color: var(--muted);
    margin-top: 3px;
  }
</style>
</head>
<body>
  <div class="business-card">
    <svg class="card-shapes" width="1018" height="262" viewBox="0 0 1018 262" aria-hidden="true">
      <polygon points="0,0 509,0 401,262 0,262" fill="var(--navy)"/>
      <polygon points="509,0 552,0 442,262 401,262" fill="var(--teal)"/>
    </svg>

    <div class="brand">Vertix Engenharia</div>

    <div class="contact-item email">
      <svg class="icon" viewBox="0 0 28 28" aria-hidden="true">
        <rect width="28" height="28" rx="3" fill="var(--navy)"/>
        <rect x="6" y="8" width="16" height="12" fill="none" stroke="#fff" stroke-width="2"/>
        <polyline points="6,8 14,15 22,8" fill="none" stroke="#fff" stroke-width="2"/>
      </svg>
      <span>vertixengenharia@com.br</span>
    </div>
    <div class="contact-item phone">
      <svg class="icon" viewBox="0 0 28 28" aria-hidden="true">
        <rect width="28" height="28" rx="3" fill="var(--navy)"/>
        <path d="M6 11 Q14 5 22 11 L20 13 L17 11 L11 11 L8 13 Z" fill="#fff"/>
        <rect x="8" y="14" width="12" height="8" rx="1" fill="#fff"/>
      </svg>
      <span>(11) 00000-0000</span>
    </div>
    <div class="contact-item web">
      <svg class="icon" viewBox="0 0 28 28" aria-hidden="true">
        <rect width="28" height="28" rx="3" fill="var(--navy)"/>
        <circle cx="14" cy="14" r="8" fill="none" stroke="#fff" stroke-width="2"/>
        <ellipse cx="14" cy="14" rx="3.5" ry="8" fill="none" stroke="#fff" stroke-width="1.5"/>
        <line x1="6" y1="14" x2="22" y2="14" stroke="#fff" stroke-width="1.5"/>
      </svg>
      <span>www.vertixengenharia.com.br</span>
    </div>
    <div class="contact-item address">
      <svg class="icon" viewBox="0 0 28 28" aria-hidden="true">
        <rect width="28" height="28" rx="3" fill="var(--navy)"/>
        <path d="M14 23 C9 16 8 14 8 12 A6 6 0 0 1 20 12 C20 14 19 16 14 23 Z" fill="#fff"/>
        <circle cx="14" cy="12" r="2.2" fill="var(--navy)"/>
      </svg>
      <span>Rua do projeto, 00 Centro - Cidade - Estado<br>&nbsp;Cep. 00.000.000</span>
    </div>

    <div class="contact-person">
      <div class="name">Nome Sobrenome</div>
      <div class="role">Diretor Comercial</div>
    </div>
  </div>
</body>
</html>
```